Tide Works - Logo & Business Card

I have briefly designed a logo for my small events business and need it fixed up. I would prefer it to be white on black background. I also need a PDF for business cards, I would like them to be black with the logo on one side and my details on the other side:

Tide Works
Corinne-Mae Talbisk
Founder / Director
0492 817 403
corinne@tideworks.com.au

Industry/Entity Type

Events

```html
<!DOCTYPE html>
<html lang="en">
<head>
<meta charset="utf-8">
<title>Tide Works – Business Cards</title>
<link rel="stylesheet" href="https://fonts.googleapis.com/css2?family=Questrial&display=swap">
<style>
  :root {
    --stage: #6e4229;
    --card-black: #050505;
    --card-white: #ffffff;
    --teal: #2fbfa8;
    --teal-line: #6fd8cb;
    --card-shadow: rgba(0, 0, 0, 0.35);
  }
  * { margin: 0; padding: 0; box-sizing: border-box; }
  html, body {
    width: 1200px;
    height: 914px;
    overflow: hidden;
    background: var(--stage);
    font-family: "Questrial", sans-serif;
  }
  .canvas {
    position: relative;
    width: 1200px;
    height: 914px;
  }
  .card {
    position: absolute;
    left: 280px;
    width: 640px;
    height: 390px;
    overflow: hidden;
    box-shadow: 0 10px 28px var(--card-shadow);
  }
  .card--front { top: 46px; background: var(--card-white); }
  .card--back  { top: 478px; background: var(--card-black); }

  /* Front: black band over white, brand centred on the seam */
  .front-band {
    position: absolute;
    left: 0; top: 0;
    width: 100%;
    height: 42%;
    background: var(--card-black);
  }
  .brand {
    position: absolute;
    display: flex;
    align-items: center;
    gap: 12px;
    color: var(--teal);
    font-weight: 400;
    white-space: nowrap;
  }
  .brand-dot {
    border-radius: 50%;
    background: var(--teal);
    flex: none;
  }
  .card--front .brand {
    left: 50%;
    top: 58%;
    transform: translate(-50%, -50%);
    font-size: 46px;
  }
  .card--front .brand-dot { width: 22px; height: 22px; }

  /* Back: white brand panel, teal rule, black details panel */
  .back-brand-panel {
    position: absolute;
    left: 0; top: 0;
    width: 36%;
    height: 100%;
    background: var(--card-white);
  }
  .back-rule {
    position: absolute;
    left: calc(36% + 6px);
    top: 0;
    width: 4px;
    height: 100%;
    background: var(--teal-line);
  }
  .card--back .brand {
    left: 18%;
    top: 48%;
    transform: translate(-50%, -50%);
    font-size: 27px;
    gap: 8px;
  }
  .card--back .brand-dot { width: 13px; height: 13px; }

  .details {
    position: absolute;
    left: calc(36% + 40px);
    top: 64px;
    color: var(--teal);
  }
  .details-name { font-size: 25px; font-weight: 400; letter-spacing: 0.3px; }
  .details-role { font-size: 18px; margin-top: 4px; }

  .contact {
    position: absolute;
    left: calc(36% + 40px);
    bottom: 62px;
    list-style: none;
    color: var(--teal);
    font-size: 19px;
  }
  .contact-item {
    display: flex;
    align-items: center;
    gap: 10px;
    line-height: 1.45;
  }
  .contact-icon { width: 14px; height: 14px; flex: none; }
</style>
</head>
<body>
<main class="canvas">

  <section class="card card--front" aria-label="Business card front">
    <div class="front-band"></div>
    <div class="brand">
      <span class="brand-dot"></span>
      <span class="brand-name">Tide Works</span>
    </div>
  </section>

  <section class="card card--back" aria-label="Business card back">
    <div class="back-brand-panel"></div>
    <div class="back-rule"></div>
    <div class="brand">
      <span class="brand-dot"></span>
      <span class="brand-name">Tide Works</span>
    </div>

    <div class="details">
      <h1 class="details-name">Corinne-Mae Talbisk</h1>
      <p class="details-role">Founder / Director</p>
    </div>

    <ul class="contact">
      <li class="contact-item">
        <svg class="contact-icon" viewBox="0 0 14 14" aria-hidden="true">
          <rect x="3.5" y="0.8" width="7" height="12.4" rx="1.4" fill="none" stroke="#ffffff" stroke-width="1.3"/>
          <rect x="5" y="2.6" width="4" height="5" fill="#ffffff"/>
          <circle cx="7" cy="10.6" r="0.9" fill="#ffffff"/>
        </svg>
        <span>0492 817 403</span>
      </li>
      <li class="contact-item">
        <svg class="contact-icon" viewBox="0 0 14 14" aria-hidden="true">
          <rect x="0.8" y="3" width="12.4" height="8.4" fill="none" stroke="#ffffff" stroke-width="1.2"/>
          <path d="M0.8 3 L7 8 L13.2 3" fill="none" stroke="#ffffff" stroke-width="1.2"/>
        </svg>
        <span>corinne@tideworks.com.au</span>
      </li>
    </ul>
  </section>

</main>
</body>
</html>
```